Startseite gestalten!
Zielgruppe
20 - 45 Jahre alt, legt Wert auf Mode usw.
Hallo,
ich suche jemanden, der mir die Startseite von K&W stoffwerk (www.kw-stoffwerk.com) chic gestalten kann.
Die Elemente, die jetzt drauf sind sollen bleiben... es geht nur noch um die Gestaltung.
Also Video, Blog und 2 "Werbeflächen" sollen bleiben....
Ebenso die Grundfarbgestaltung usw.
Soll halt schön in die restl. Seite passen.
Freue mich auf die Entwürfe!

```html
<!DOCTYPE html>
<html lang="de">
<head>
<meta charset="utf-8">
<title>K&amp;W stoffwerk – Startseite</title>
<link rel="stylesheet" href="https://fonts.googleapis.com/css2?family=Oswald:wght@400;500&family=Arimo:wght@400;700&display=swap">
<style>
  :root {
    --black: #000000;
    --white: #ffffff;
    --blue: #0a9fdd;
    --band: #eeeeee;
    --grey-text: #777777;
    --player-grey: #d9d9d9;
  }
  * { box-sizing: border-box; margin: 0; padding: 0; }
  html, body { width: 1200px; height: 900px; overflow: hidden; background: var(--white); }
  body { position: relative; font-family: "Arimo", Arial, sans-serif; color: var(--black); }

  .site-header {
    position: absolute; left: 93px; top: 0; width: 998px; height: 105px;
    background: var(--black);
  }
  .brand {
    position: absolute; left: 0; top: 0; width: 139px; height: 105px;
    border-right: 1px solid #555;
    display: flex; flex-direction: column; align-items: center; justify-content: center;
    color: var(--white); font-family: "Oswald", sans-serif; font-weight: 400;
  }
  .brand-name { font-size: 34px; line-height: 1; }
  .brand-sub { font-size: 13px; margin-top: 6px; letter-spacing: .5px; }
  .main-nav a {
    position: absolute; top: 36px; transform: translateX(-50%);
    color: var(--white); text-decoration: none;
    font-family: "Oswald", sans-serif; font-weight: 500; font-size: 22px; white-space: nowrap;
  }

  .hero-photo {
    position: absolute; left: 93px; top: 111px; width: 489px; height: 212px;
    background: linear-gradient(180deg, #f2f2f2 0%, #e4e4e4 45%, #5a5a5a 58%, #7c7c7c 66%, #b9b9b9 82%, #a4a4a4 100%);
  }
  .blog-teaser {
    position: absolute; left: 584px; top: 111px; width: 244px; height: 212px;
    background: var(--blue); color: var(--white); text-decoration: none;
  }
  .blog-teaser .teaser-brand {
    position: absolute; left: 0; right: 0; top: 40px; text-align: center;
    font-family: "Oswald", sans-serif; font-weight: 400;
  }
  .teaser-brand .brand-name { font-size: 36px; line-height: 1; display: block; }
  .teaser-brand .brand-sub { font-size: 12px; display: block; margin-top: 6px; }
  .blog-teaser .teaser-text {
    position: absolute; left: 23px; top: 154px; width: 172px;
    font-family: "Oswald", sans-serif; font-size: 14px; line-height: 1.4;
  }
  .blog-teaser svg { position: absolute; left: 213px; top: 167px; }

  .video-box {
    position: absolute; left: 836px; top: 111px; width: 255px; height: 212px;
    background: var(--black);
  }
  .video-frame {
    position: absolute; left: 10px; top: 24px; width: 235px; height: 165px;
    background: linear-gradient(180deg, #b9d3a6 0%, #7ea365 30%, #4f6f3e 55%, #2b2b2b 78%, #1a1a1a 100%);
  }
  .video-frame svg { position: absolute; left: 96px; top: 60px; }
  .video-controls {
    position: absolute; left: 0; top: 191px; width: 255px; height: 21px;
    background: var(--player-grey); display: flex; align-items: center; padding: 0 8px; gap: 8px;
    font-size: 9px; color: #333;
  }
  .video-track { flex: 1; height: 5px; background: #aaa; border-radius: 3px; }

  .section-head {
    position: absolute; top: 342px; height: 33px; background: var(--band);
  }
  .section-head span {
    display: inline-block; height: 33px; line-height: 33px; padding: 0 10px;
    background: var(--black); color: var(--white); font-size: 12px; font-weight: 700; letter-spacing: .3px;
  }

  .product { position: absolute; top: 392px; width: 200px; height: 230px; }
  .product-title { font-size: 16px; font-weight: 700; }
  .product-sub { font-size: 10px; color: var(--grey-text); margin-top: 4px; letter-spacing: .3px; }
  .product-image {
    position: absolute; left: -6px; top: 62px; width: 140px; height: 138px;
    border-radius: 10px 10px 4px 4px;
    background: linear-gradient(180deg, #262626 0%, #0c0c0c 60%, #000 100%);
  }
  .price-tag {
    position: absolute; left: 5px; top: 166px; width: 77px; height: 35px;
    background: var(--blue); color: var(--white); font-size: 16px;
    display: flex; align-items: center; justify-content: center;
  }
  .order-link {
    position: absolute; left: 0; top: 212px; font-size: 12px; color: var(--black);
    text-decoration: none; white-space: nowrap;
  }

  .preorder-ad {
    position: absolute; left: 788px; top: 395px; width: 303px; height: 223px;
    background: linear-gradient(180deg, #1e1e1e 0%, #4a4a4a 35%, #5b5a8c 55%, #8d8d8d 75%, #a9a9a9 100%);
    color: var(--white); text-decoration: none;
  }
  .preorder-ad .ad-brand {
    position: absolute; left: 115px; top: 6px; text-align: center;
    font-family: "Oswald", sans-serif;
  }
  .ad-brand .brand-name { font-size: 26px; line-height: 1; display: block; }
  .ad-brand .brand-sub { font-size: 10px; display: block; margin-top: 3px; }
  .preorder-ad .ad-url { position: absolute; left: 12px; top: 184px; font-family: "Oswald", sans-serif; font-size: 12px; }
  .preorder-ad .ad-title { position: absolute; left: 12px; top: 198px; font-family: "Oswald", sans-serif; font-size: 16px; white-space: nowrap; }

  .site-footer {
    position: absolute; left: 524px; top: 671px; width: 567px; height: 41px;
    background: var(--black);
  }
  .site-footer a {
    position: absolute; top: 11px; transform: translateX(-50%);
    color: var(--white); text-decoration: none;
    font-family: "Oswald", sans-serif; font-weight: 500; font-size: 14px; white-space: nowrap;
  }
</style>
</head>
<body>
  <header class="site-header">
    <div class="brand"><span class="brand-name">K&amp;W</span><span class="brand-sub">stoffwerk</span></div>
    <nav class="main-nav">
      <a href="#" style="left:272px">Home</a>
      <a href="#" style="left:402px">K&amp;W Shop</a>
      <a href="#" style="left:539px">Charity</a>
      <a href="#" style="left:669px">Über uns</a>
      <a href="#" style="left:824px">Impressionen</a>
    </nav>
  </header>

  <div class="hero-photo" role="img" aria-label="Schwarz-weißes Foto zweier Polospieler zu Pferd auf dem Spielfeld"></div>

  <a class="blog-teaser" href="#">
    <div class="teaser-brand"><span class="brand-name">K&amp;W</span><span class="brand-sub">stoffwerk</span></div>
    <p class="teaser-text">Besuchen Sie jetzt unseren<br>Blog und erfahren neues</p>
    <svg width="10" height="14" viewBox="0 0 10 14"><path d="M2 2 L7 7 L2 12" fill="none" stroke="#fff" stroke-width="2"/></svg>
  </a>

  <div class="video-box">
    <div class="video-frame" role="img" aria-label="Videovorschau: zwei Polospieler im Interview vor Pferden">
      <svg width="44" height="44" viewBox="0 0 44 44"><rect width="44" height="44" rx="8" fill="#000" fill-opacity=".45"/><path d="M17 12 L32 22 L17 32 Z" fill="#fff"/></svg>
    </div>
    <div class="video-controls">
      <svg width="8" height="9" viewBox="0 0 8 9"><path d="M0 0 L8 4.5 L0 9 Z" fill="#333"/></svg>
      <div class="video-track"></div>
      <span>0:00 / 0:00</span>
    </div>
  </div>

  <div class="section-head" style="left:93px;width:680px"><span>BELIEBTESTE ARTIKEL</span></div>
  <div class="section-head" style="left:785px;width:306px"><span>JETZT VORBESTELLEN</span></div>

  <article class="product" style="left:125px">
    <h3 class="product-title">Shirt für Männer</h3>
    <p class="product-sub">TAILLIERTES MEN-SHIRT</p>
    <div class="product-image" role="img" aria-label="Schwarzes T-Shirt mit blauem Polomotiv"></div>
    <div class="price-tag">25.00 €</div>
    <a class="order-link" href="#">Jetzt bestellen &gt;</a>
  </article>
  <article class="product" style="left:350px">
    <h3 class="product-title">Team Shirt 2008</h3>
    <p class="product-sub">LANGARMSHIRT</p>
    <div class="product-image" role="img" aria-label="Schwarzes Langarm-Poloshirt mit Rückennummer 3"></div>
    <div class="price-tag">25.00 €</div>
    <a class="order-link" href="#">Jetzt bestellen &gt;</a>
  </article>
  <article class="product" style="left:573px">
    <h3 class="product-title">Team Shirt 2008</h3>
    <p class="product-sub">KURZARMSHIRT</p>
    <div class="product-image" role="img" aria-label="Schwarzes Kurzarm-Poloshirt mit Rückennummer 3"></div>
    <div class="price-tag">49.00 €</div>
    <a class="order-link" href="#">Jetzt bestellen &gt;</a>
  </article>

  <a class="preorder-ad" href="#" role="img" aria-label="Werbefläche: blaue Team-Poloshirts und gezeichneter Polospieler, Oktoberfest-Teamshirt 2009">
    <div class="ad-brand"><span class="brand-name">K&amp;W</span><span class="brand-sub">stoffwerk</span></div>
    <span class="ad-url">www.kw-stoffwerk.com</span>
    <span class="ad-title">OKTOBERFEST-TEAMSHIRT 2009</span>
  </a>

  <footer class="site-footer">
    <a href="#" style="left:71px">Links</a>
    <a href="#" style="left:151px">Kontakt</a>
    <a href="#" style="left:246px">Impressum</a>
    <a href="#" style="left:331px">AGB</a>
    <a href="#" style="left:446px">Datenschutzerklärung</a>
  </footer>
</body>
</html>
```